Design Large Inspirational Artwork with Long Quote

Design a large piece of art with a quote from Marcus Hallwell.

QUOTE
"The thing that's so interesting about being alive is that you're all in. No matter what you do, you're all in. This is gonna kill you, so I think you might as well play the most magnificent game you can while you're waiting. Because, do you have anything better to do? Why not pick the best thing possible that you could do? Because you're more powerful than you think, way more powerful than you think. I mean, God only knows what you are in the final analysis. You're blind to your own weaknesses, but you're also blind to your own strengths. How far could you take that if you stopped wasting time, and if you stopped lying, and if you oriented yourself to the highest possible good that you could conceive of and you committed to that? How much good could you do? Well, I would say: why don't you find out?"

SIZE
A high-resolution print size of 6' wide and 3' tall should provide ample space for both the quote and the accompanying artwork.

TYPOGRAPHY
Choose a bold, clean, and easily readable font for the quote. You could also experiment with different font sizes for certain words or phrases to emphasize their importance within the quote.

COLORS
Since the quote is thought-provoking and reflective, you might want to use a color palette that evokes a sense of introspection and depth. Consider using cool, calming colors like shades of blue, gray, or green. Alternatively, you can use a contrasting color scheme with a light background and dark text to make the quote stand out.

ARTWORK
Select / create / edit background artwork to complement the quote.
While a great design might be minimalistic and/or greyscale, I'd really like to see some full color options. This might be anything from photography or graphics inspired by the ideas in the text, to abstract colors or illustrations that feel like the sentiment expressed.
The art should capture your attention and encourage you to read the text. The art should be visually appealing, both at a distance and up close, regardless of whether the text is read.
Updates

Having trouble confirming the exact print size.

Still looking for printing solution and final size confirmation.

Target Market(s)

Personal, business, office

Industry/Entity Type

None

Font styles to use
Sans Serif
Script

Requirements
Must have
• Entire quote, legible text, modern design, attractive artwork, approx 6ft wide and 3ft tall
Nice to have
• Different font (sizes) for certain words or phrases to emphasize their importance within the quote.

```html
<!DOCTYPE html>
<html lang="en">
<head>
<meta charset="utf-8">
<title>All In — Marcus Hallwell Quote Art</title>
<link href="https://fonts.googleapis.com/css2?family=Quicksand:wght@500;700&display=swap" rel="stylesheet">
<style>
  :root {
    --ink: #151515;
    --accent: #e3000e;
    --light: #ffffff;
    --mist-top: #e4e8ea;
    --mist-mid: #c3ccd1;
    --slate: #7f8b93;
    --rock: #3b3f42;
  }
  html, body {
    margin: 0;
    padding: 0;
    width: 1200px;
    height: 603px;
    overflow: hidden;
    background: #ffffff;
  }
  .artwork {
    position: relative;
    width: 1200px;
    height: 603px;
    overflow: hidden;
    font-family: "Quicksand", sans-serif;
    font-weight: 500;
    color: var(--ink);
  }
  .backdrop {
    position: absolute;
    inset: 0;
    background:
      radial-gradient(ellipse 70% 60% at 30% 20%, var(--mist-top) 0%, rgba(228,232,234,0) 70%),
      linear-gradient(170deg, var(--mist-top) 0%, var(--mist-mid) 45%, var(--slate) 78%, var(--rock) 100%);
  }
  .quote {
    position: absolute;
    margin: 0;
    font-size: 23px;
    line-height: 31.5px;
    letter-spacing: 0.1px;
  }
  .quote-opening {
    left: 24px;
    top: 12px;
  }
  .quote-reflection {
    right: 68px;
    top: 273px;
    text-align: right;
    font-size: 21.5px;
    line-height: 29.6px;
  }
  .quote line, .line { display: block; white-space: nowrap; }
  .emphasis {
    color: var(--accent);
    font-weight: 700;
    font-style: italic;
  }
  .aside {
    font-style: italic;
    font-weight: 700;
    margin-bottom: 4px;
  }
  .quote-closing {
    position: absolute;
    left: 0;
    width: 1234px;
    top: 555px;
    margin: 0;
    text-align: center;
    color: var(--light);
    font-weight: 700;
    font-style: italic;
    font-size: 27px;
    letter-spacing: 0.5px;
    text-transform: uppercase;
  }
  .attribution {
    position: absolute;
    right: 10px;
    top: 580px;
    margin: 0;
    color: var(--light);
    font-size: 13.5px;
  }
</style>
</head>
<body>
  <main class="artwork">
    <div class="backdrop" role="img" aria-label="Misty mountain fjord with a lone hiker in a red jacket standing on a rocky ledge at lower left"></div>

    <p class="quote quote-opening">
      <span class="line">The thing that's so interesting about being alive is that you're all in.</span>
      <span class="line">No matter what you do, you're all in.</span>
      <span class="line">This is gonna kill you, so I think you might as well play</span>
      <span class="line">the most magnificent game you can while you're waiting.</span>
      <span class="line emphasis">Because, do you have anything better to do?</span>
      <span class="line">Why not pick the best thing possible that you could do?</span>
      <span class="line emphasis">Because you're more powerful than you think,</span>
      <span class="line">way more powerful than you think.</span>
    </p>

    <p class="quote quote-reflection">
      <span class="line aside">I mean, God only knows what you are in the final analysis.</span>
      <span class="line">You're blind to your own weaknesses,</span>
      <span class="line">but you're also blind to your own strengths.</span>
      <span class="line">How far could you take that</span>
      <span class="line emphasis">if you stopped wasting time, and</span>
      <span class="line emphasis">if you stopped lying, and</span>
      <span class="line emphasis">if you oriented yourself to the highest possible good that</span>
      <span class="line">you could conceive of and you committed to that?</span>
      <span class="line">How much good could you do?</span>
    </p>

    <p class="quote-closing">Well, I would say : why don’t you find out?</p>
    <p class="attribution">- Marcus Hallwell</p>
  </main>
</body>
</html>
```